Emergency Medical Training and Events Company Business Needs Business Card Design

We are in need of a business card for our dynamic company expanding its customer base and need to be easily contacted and identified for when we visit with government officials, potential EMS / Fire agencies and county coordinators to arrange for training programs for first responders to better prepare them for critical thinking at critical incidents.

Target Market(s)

EMS/Fire and Event Promoters

Industry/Entity Type

Medical

Contact Information for Business Card

Two cards, comparable designs:

Martin K. Halvey, Principal, m.halvey@rvqtlo.com
Owen Tash, Event and Training Specialist, o.tash@rvqtlo.com

Font styles to use
Other font styles liked:
• Cambria

Colors

Designer to choose colors to be used in the design.

Requirements
Must have
• Company Logo, Spots for Name, Title, Phone Number, Email, Website
• A bullet list stating that we offer, QRB CPR and First Aid Instructors, Hold the Line Instructors, Event EMS, CME's, MCI Training and Planning. We prefer to have a black background for the card but if you can make a blue or white card stand out we would review that as well.
Should not have
• Tacky logos or special sayings ... simple, elegant, professional is the look we seek

```html
<!DOCTYPE html>
<html lang="en">
<head>
<meta charset="utf-8">
<title>RVQ Training of NY – Business Card</title>
<link href="https://fonts.googleapis.com/css2?family=Caladea:wght@400;700&family=Arimo:wght@400&family=Lato:wght@400&display=swap" rel="stylesheet">
<style>
  :root {
    --stage: #2b2b2d;
    --card-white: #ffffff;
    --navy: #1b2466;
    --navy-deep: #141b55;
    --red: #c8202b;
    --ink: #1a1a1a;
    --rule: #b9b9b9;
    --pattern: #232d74;
  }
  * { box-sizing: border-box; margin: 0; padding: 0; }
  html, body { width: 1200px; height: 1108px; overflow: hidden; }
  body {
    background: var(--stage);
    position: relative;
    font-family: "Arimo", Arial, sans-serif;
  }
  .card {
    position: absolute;
    top: 169px;
    width: 440px;
    height: 770px;
    border-radius: 22px;
    overflow: hidden;
  }
  .card--front { left: 120px; background: var(--card-white); text-align: center; }
  .card--back  { left: 640px; background: linear-gradient(180deg, var(--navy) 0%, var(--navy-deep) 100%); color: #fff; }

  .brand { position: absolute; top: 130px; left: 0; right: 0; display: flex; flex-direction: column; align-items: center; gap: 22px; }
  .brand__dot { width: 96px; height: 96px; border-radius: 50%; background: var(--navy); }
  .brand__name {
    font-family: "Caladea", Cambria, serif;
    font-weight: 700;
    font-size: 40px;
    letter-spacing: 1px;
    color: var(--navy);
    line-height: 1.1;
  }

  .person { position: absolute; top: 430px; left: 0; right: 0; }
  .person__name {
    font-family: "Caladea", Cambria, serif;
    font-size: 30px;
    letter-spacing: 1px;
    color: var(--navy);
  }
  .person__name .surname { color: var(--red); }
  .person__title { font-size: 21px; color: var(--ink); margin-top: 4px; }

  .divider { position: absolute; top: 520px; left: 60px; right: 60px; display: flex; align-items: center; gap: 10px; }
  .divider__rule { flex: 1; height: 1px; background: var(--rule); }
  .icon { width: 30px; height: 30px; border-radius: 5px; background: var(--navy); display: flex; align-items: center; justify-content: center; }
  .icon--mail { background: var(--red); }

  .contact { position: absolute; top: 575px; left: 0; right: 0; font-size: 21px; color: var(--ink); line-height: 1.45; }
  .contact__web { color: var(--navy); }
  .contact__web .domain { color: var(--red); }

  .back__pattern {
    position: absolute; left: 0; right: 0; top: 0; height: 520px;
    background: linear-gradient(180deg, var(--pattern) 0%, rgba(35,45,116,0) 100%);
  }
  .back__mark { position: absolute; top: 355px; left: 50%; width: 70px; height: 70px; margin-left: -35px; border-radius: 50%; background: #fff; }
  .services {
    position: absolute; bottom: 80px; left: 0; right: 0;
    list-style: none; text-align: center;
    font-family: "Lato", Arial, sans-serif; font-size: 23px; line-height: 1.3;
  }
</style>
</head>
<body>
  <section class="card card--front">
    <div class="brand">
      <span class="brand__dot"></span>
      <span class="brand__name">RVQ TRAINING<br>OF NY</span>
    </div>
    <div class="person">
      <p class="person__name">OWEN <span class="surname">TASH</span></p>
      <p class="person__title">Event and Training Specialist</p>
    </div>
    <div class="divider">
      <span class="divider__rule"></span>
      <span class="icon">
        <svg width="18" height="18" viewBox="0 0 24 24"><path fill="#fff" d="M6.6 10.8a15 15 0 0 0 6.6 6.6l2.2-2.2a1 1 0 0 1 1-.25 11.4 11.4 0 0 0 3.6.57 1 1 0 0 1 1 1V20a1 1 0 0 1-1 1A17 17 0 0 1 3 4a1 1 0 0 1 1-1h3.5a1 1 0 0 1 1 1c0 1.25.2 2.45.57 3.57a1 1 0 0 1-.25 1z"/></svg>
      </span>
      <span class="icon icon--mail">
        <svg width="18" height="18" viewBox="0 0 24 24"><rect x="3" y="5" width="18" height="14" fill="none" stroke="#fff" stroke-width="2"/><path d="M3 6l9 7 9-7" fill="none" stroke="#fff" stroke-width="2"/></svg>
      </span>
      <span class="icon">
        <svg width="18" height="18" viewBox="0 0 24 24"><path fill="#fff" d="M12 2a7 7 0 0 0-7 7c0 5 7 13 7 13s7-8 7-13a7 7 0 0 0-7-7zm0 9.5A2.5 2.5 0 1 1 12 6.5a2.5 2.5 0 0 1 0 5z"/></svg>
      </span>
      <span class="divider__rule"></span>
    </div>
    <div class="contact">
      <p>5550 140273</p>
      <p>o.tash@rvqtlo.com</p>
      <p class="contact__web">www.<span class="domain">rvqtlo</span>.com</p>
    </div>
  </section>

  <section class="card card--back">
    <div class="back__pattern" role="img" aria-label="Faint repeating emblem pattern"></div>
    <span class="back__mark"></span>
    <ul class="services">
      <li>QRB CPR and First Aid Instructors</li>
      <li>Hold the Line Instructors</li>
      <li>We do Event EMS &nbsp;|&nbsp; CME's</li>
      <li>MCI Training and Planning</li>
    </ul>
  </section>
</body>
</html>
```